Ridgeway Moss - Facebook Cover Photo & Photo Icon Design

We’re looking for a Facebook Cover Photo and Profile Icon design for Ridgeway Moss, a leading Residential Real Estate brand under Ridgeway Property Agents, based in Capalaba and Alexandra Hills, Queensland, Australia.

This design will represent my professional real estate profile and needs to be bold, clean, and on-brand.

Deliverables:

Facebook Cover Photo (820 x 312 px, optimized for mobile + desktop)

Facebook Profile Icon (1:1 ratio, minimum 320 x 320 px)

Design Guidelines:

1. Must Include:

The Ridgeway Moss logo (provided after project start)

Use of the Ridgeway Property Agents brand colour palette (will be supplied)

Clear connection to residential real estate

2. Optional but Preferred:

A local photo or skyline of Capalaba or Alexandra Hills in QLD (bonus points for this)

Space for a short tagline like:
“Selling Faster. Selling Smarter. Selling Ridgeway.”
(Optional tagline – open to variations if it improves layout/design)

3. Style & Feel:

Professional yet personable

Clean, modern aesthetic

Subtle touches of fun or personality are welcome

Layout must work well when overlaid by Facebook UI elements (like profile photo & call-to-action buttons)

Who I Am:
I'm a well-known residential real estate agent in the Redlands area, known for high-energy campaigns, premium video marketing, and a results-driven approach. My brand is fun, fresh, and high-performing — just like the real estate campaigns I run.

Files to be Provided (after selection):

Ridgeway Moss logo in high-res

Brand colour palette / style reference

Optional photo references if local imagery is not sourced by designer

Final Notes:

Make sure all text is legible on mobile and desktop

Original, layered design files must be delivered (PSD or AI preferred)

Bonus points if it feels uniquely “Bayside Queensland” while maintaining a national-level professional polish

Target Market(s)

Alexandra Hills, Capalaba & Sheldon

Industry/Entity Type

Real Estate

Colors
0054AA
0677BA
7BADD7
CADEEF
E8F1F8

Requirements
Must have
• Headshot, Mobile Number 0491 726 805, Suburbs - Alexandra Hills, Capalaba & Sheldon
Nice to have
• White, Crisp & Professional. Bottom Banner with Suburb List. Specialising in Alexandra Hills, Capalaba & Sheldon

```html
<!DOCTYPE html>
<html lang="en">
<head>
<meta charset="utf-8">
<title>Ridgeway Moss – Facebook Cover &amp; Profile Icon</title>
<link rel="stylesheet" href="https://fonts.googleapis.com/css2?family=Saira+Condensed:wght@400;500;600&family=Mulish:wght@300;400;500&display=swap">
<style>
  :root {
    --stage: #3a2a20;
    --navy-deep: rgba(28, 48, 128, 0.88);
    --sand-light: #d9c8a0;
    --sand: #b8a77c;
    --haze: #c9c0a6;
    --tan: #dba569;
    --white: #ffffff;
    --suit: #3d4a5c;
    --suit-dark: #26303f;
  }
  * { margin: 0; padding: 0; box-sizing: border-box; }
  html, body { width: 1200px; height: 447px; overflow: hidden; }
  body { background: var(--stage); position: relative; font-family: "Mulish", sans-serif; color: var(--white); }

  .cover, .profile-icon { position: absolute; overflow: hidden; }
  .cover { left: 35px; top: 34px; width: 775px; height: 295px; }
  .profile-icon { left: 829px; top: 26px; width: 303px; height: 303px; }

  .aerial-photo { position: absolute; inset: 0; }
  .cover .aerial-photo { background: linear-gradient(180deg, var(--haze) 0%, var(--sand-light) 30%, var(--sand) 60%, #8f8a6e 100%); }
  .profile-icon .aerial-photo { background: linear-gradient(160deg, #c7b387 0%, #b79f72 55%, #6f7c86 100%); }

  .brand-wedge { position: absolute; inset: 0; width: 100%; height: 100%; }

  .headshot { position: absolute; background: linear-gradient(180deg, #6b7685 0%, var(--suit) 45%, var(--suit-dark) 100%); border-radius: 48% 48% 0 0 / 30% 30% 0 0; }
  .cover .headshot { left: 0; top: 26px; width: 250px; height: 269px; }
  .profile-icon .headshot { left: 4px; top: 137px; width: 150px; height: 166px; }

  .wordmark { position: absolute; text-align: center; font-family: "Mulish", sans-serif; font-weight: 300; color: var(--white); line-height: 1; letter-spacing: 0.08em; }
  .wordmark-top, .wordmark-main { display: block; }
  .cover .wordmark { left: 250px; top: 24px; width: 210px; }
  .cover .wordmark-top { font-size: 22px; }
  .cover .wordmark-main { font-size: 60px; margin-top: 2px; }
  .profile-icon .wordmark { right: 11px; top: 170px; width: 140px; text-align: right; }
  .profile-icon .wordmark-top { font-size: 15px; }
  .profile-icon .wordmark-main { font-size: 36px; margin-top: 1px; }

  .phone { position: absolute; display: flex; align-items: center; gap: 10px; font-family: "Saira Condensed", sans-serif; font-weight: 500; line-height: 1; }
  .phone svg { flex: none; }
  .cover .phone { right: 21px; top: 89px; font-size: 31px; color: var(--tan); }
  .profile-icon .phone { left: 11px; top: 83px; font-size: 31px; color: var(--white); }

  .tagline { position: absolute; font-family: "Saira Condensed", sans-serif; font-weight: 500; line-height: 1.12; }
  .cover .tagline { right: 13px; top: 136px; text-align: right; font-size: 33px; }
  .profile-icon .tagline { left: 11px; top: 12px; font-size: 26px; line-height: 1.14; }

  .brand-line { position: absolute; right: 13px; top: 226px; font-size: 13px; letter-spacing: 0.02em; }

  .agent { position: absolute; line-height: 1; }
  .cover .agent { right: 13px; top: 252px; }
  .cover .agent-name { font-weight: 500; font-size: 17px; color: var(--tan); }
  .cover .agent-role { font-size: 13px; color: var(--white); }
  .suburbs { position: absolute; right: 13px; top: 276px; font-size: 11px; letter-spacing: 0.04em; color: var(--white); }
  .profile-icon .agent { right: 11px; top: 238px; text-align: right; font-family: "Saira Condensed", sans-serif; font-weight: 600; font-size: 22px; line-height: 1.25; color: var(--tan); }
  .profile-icon .agent span { display: block; }
</style>
</head>
<body>

<section class="cover" aria-label="Facebook cover, 820 by 312">
  <div class="aerial-photo" role="img" aria-label="Aerial photo of bayside suburbs with the bay and horizon beyond"></div>
  <svg class="brand-wedge" viewBox="0 0 775 295" preserveAspectRatio="none" aria-hidden="true">
    <polygon points="775,0 775,295 238,295" fill="var(--navy-deep)"/>
  </svg>
  <div class="headshot" role="img" aria-label="Headshot of the agent in a blue blazer and white shirt"></div>

  <div class="wordmark"><span class="wordmark-top">RIDGEWAY</span><span class="wordmark-main">MOSS</span></div>

  <div class="phone">
    <svg width="28" height="28" viewBox="0 0 24 24" fill="none" stroke="currentColor" stroke-width="1.5" stroke-linejoin="round" aria-hidden="true">
      <path d="M5 3h3.5l1.8 4.6-2.3 1.5a11 11 0 0 0 5.9 5.9l1.5-2.3L20 14.5V18a2 2 0 0 1-2 2A15 15 0 0 1 3 5a2 2 0 0 1 2-2z"/>
      <path d="M14.5 3.5a6 6 0 0 1 6 6M14.5 7a2.6 2.6 0 0 1 2.5 2.5"/>
    </svg>
    <span>0491 726 805</span>
  </div>

  <p class="tagline">Selling Faster. Selling Smarter.<br>Selling Ridgeway.</p>
  <p class="brand-line">Leading Residential Real Estate brand under Ridgeway Property Agents</p>
  <p class="agent"><span class="agent-name">Rowan Moss,</span> <span class="agent-role">Suburb Specialist</span></p>
  <p class="suburbs">Alexandra Hills · Capalaba · Sheldon</p>
</section>

<section class="profile-icon" aria-label="Facebook profile icon, 320 by 320">
  <div class="aerial-photo" role="img" aria-label="Photo of a coastal high-rise skyline beside the water"></div>
  <svg class="brand-wedge" viewBox="0 0 303 303" preserveAspectRatio="none" aria-hidden="true">
    <polygon points="303,0 303,303 0,303 0,276" fill="var(--navy-deep)"/>
  </svg>
  <div class="headshot" role="img" aria-label="Headshot of the agent in a blue blazer and white shirt"></div>

  <p class="tagline">Selling Faster. Selling Smarter.<br>Selling Ridgeway.</p>

  <div class="phone">
    <svg width="30" height="30" viewBox="0 0 24 24" fill="none" stroke="currentColor" stroke-width="1.5" stroke-linejoin="round" aria-hidden="true">
      <path d="M5 3h3.5l1.8 4.6-2.3 1.5a11 11 0 0 0 5.9 5.9l1.5-2.3L20 14.5V18a2 2 0 0 1-2 2A15 15 0 0 1 3 5a2 2 0 0 1 2-2z"/>
      <path d="M14.5 3.5a6 6 0 0 1 6 6M14.5 7a2.6 2.6 0 0 1 2.5 2.5"/>
    </svg>
    <span>0491 726 805</span>
  </div>

  <div class="wordmark"><span class="wordmark-top">RIDGEWAY</span><span class="wordmark-main">MOSS</span></div>

  <p class="agent"><span>Rowan Moss</span><span>Suburb Specialist</span></p>
</section>

</body>
</html>
```